Business Card Design

We need a new buisness card designed for a new company in Darwin
We dig trenchs and lay pipes for the communication industry,Electrical industry, Teleco industry,
We also do some concrete works as well,
And small excavation work
Communication
Belvanti Contracting PTY LTD
Pit and Pipe installations
Trenching,Excavations, Concreting ,
civil works, rigistrut soloutions ,over thirty years experiance
NO TRENCH TOO DEEP, NO PIPE TOO LONG
Contact Glen 0491536208 ps
(would like name to stand out somehow in another text or graphic sort of a way am also looking for some sort of slogan) will most likely be a red card with black writing

```html
<!DOCTYPE html>
<html lang="en">
<head>
<meta charset="utf-8">
<title>Belvanti Contracting – Business Card</title>
<link rel="stylesheet" href="https://fonts.googleapis.com/css2?family=Open+Sans:wght@600;700;800&display=swap">
<style>
  :root {
    --page-grey: #c4c4c4;
    --card-white: #ffffff;
    --brand-orange: #f6a21c;
    --accent-red: #e8222a;
    --panel-black: #111111;
    --panel-black-soft: #2a2a2a;
    --ink-dark: #1b1b1b;
    --text-light: #f4f4f4;
  }
  * { margin: 0; padding: 0; box-sizing: border-box; }
  html, body {
    width: 1200px;
    height: 900px;
    overflow: hidden;
    background: var(--page-grey);
    font-family: "Open Sans", sans-serif;
  }
  .canvas {
    width: 1200px;
    height: 900px;
    display: flex;
    align-items: center;
    justify-content: center;
  }
  .business-card {
    width: 1000px;
    height: 572px;
    border-radius: 30px;
    overflow: hidden;
    background: var(--card-white);
    display: flex;
    flex-direction: column;
    box-shadow: 0 12px 30px rgba(0,0,0,0.18);
  }
  .brand-area {
    height: 250px;
    padding: 70px 0 0 56px;
    display: flex;
    flex-direction: column;
    gap: 14px;
  }
  .brand-name {
    display: flex;
    align-items: center;
    gap: 18px;
    font-weight: 800;
    font-size: 52px;
    line-height: 1;
    color: var(--brand-orange);
    letter-spacing: 0.5px;
  }
  .brand-square {
    width: 46px;
    height: 46px;
    background: var(--brand-orange);
    flex-shrink: 0;
  }
  .slogan {
    font-weight: 800;
    font-size: 21px;
    letter-spacing: 1.2px;
    color: var(--ink-dark);
    text-transform: uppercase;
  }
  .contact-band {
    height: 48px;
    background: var(--brand-orange);
    display: flex;
    align-items: center;
    justify-content: center;
    gap: 56px;
    font-weight: 700;
    font-size: 27px;
    color: var(--accent-red);
  }
  .contact-item {
    display: flex;
    align-items: center;
    gap: 12px;
  }
  .contact-icon { width: 34px; height: 24px; }
  .services-panel {
    flex: 1;
    background: linear-gradient(180deg, var(--panel-black-soft) 0%, var(--panel-black) 55%, #050505 100%);
    padding: 26px 0 0 60px;
  }
  .service-list { list-style: none; }
  .service-list li {
    display: flex;
    align-items: center;
    gap: 22px;
    font-weight: 600;
    font-size: 27px;
    line-height: 1.45;
    color: var(--text-light);
  }
  .service-list li::before {
    content: "";
    width: 15px;
    height: 15px;
    border-radius: 50%;
    background: var(--accent-red);
    flex-shrink: 0;
  }
</style>
</head>
<body>
<main class="canvas">
  <article class="business-card">
    <header class="brand-area">
      <h1 class="brand-name"><span class="brand-square"></span>Belvanti Contracting PTY LTD</h1>
      <p class="slogan">No trench too deep, no pipe too long</p>
    </header>

    <section class="contact-band">
      <span class="contact-item">
        <svg class="contact-icon" viewBox="0 0 34 24" aria-hidden="true">
          <rect x="0" y="6" width="10" height="12" fill="#e8222a"/>
          <path d="M10 8h14l-4-5h4l8 9-8 9h-4l4-5H10z" fill="#e8222a"/>
        </svg>
        Contact Glen
      </span>
      <span class="contact-item">
        <svg class="contact-icon" viewBox="0 0 34 24" aria-hidden="true">
          <path d="M4 9c0-4 6-6 13-6s13 2 13 6v2h-7V8h-12v3H4z" fill="#e8222a"/>
          <path d="M9 12h16l4 9H5z" fill="#e8222a"/>
          <circle cx="17" cy="16.5" r="2.6" fill="#f6a21c"/>
        </svg>
        0491536208
      </span>
    </section>

    <section class="services-panel">
      <ul class="service-list">
        <li>Pit and Pipe installations Trenching</li>
        <li>Excavations, Concreting</li>
        <li>civil works</li>
        <li>rigistrut soloutions</li>
      </ul>
    </section>
  </article>
</main>
</body>
</html>
```